Functional Beverage Bottle Labele

I need a label created for a functional beverage. A functional beverage is a drink that provides a function as well as being a beverage. This drink aims to help ease stress and allow women to relax at the end of their day. It has been designed specifically with women in mind (men can also drink it though).

The brand values are:
Natural - we use nature to nurture our best selves, Nourishing - in the ingredients we use and messages we share, Nimble - in the way we respond to our customers and operate on a daily basis

I am looking for a modern, clean looking label. The label will be going on to a clear 330ml flint ROPP bottle, with a silver ROPP cap and contains a light pink liquid. I have attached a mock up for you to see the colour of the liquid and the style of the bottle.

I have included further information in the design brief, colour palette, logo and other items to assist you with the process of designing the label. Happy to answer any questions. I am based in Melbourne Australia.

I have uploaded the files individually and as a zip file.

Target Market(s)

Australian females aged from 21 - 60

Font styles to use
Serif
Sans Serif
Decorative
Script

Requirements
Must have
• Required on the front of the label:

Brand Logo - attached

Drink function - the function of this drink is RELAX. There will be two others in the product line, REVIVE and RECOVER. Please include RELAX somewhere on the front.

Drink flavour
Native Strawberry Gum

Drink measurement
330mL

Product description
Sparkling water with adaptogens to help you adapt to life stressors

Key call outs - 100% natural, Sugar free

There are other requirements for the remainder of the label that I have included in the document attached.
Nice to have
• Please feel free to add icons, lines, etc to make the design the best it can be and give it some personality.

The map of Victoria that I have asked to be included should not be on the front and it should be no bigger than the barcode.
Should not have
• UPDATED: There should be no strawberry images on the bottle. The Native Strawberry Gum flavour comes from the leaves of a type of eucalyptus tree grown in Australia. I have added a photo of the leaves.

```html
<!DOCTYPE html>
<html lang="en">
<head>
<meta charset="utf-8">
<title>Solace Drinks – Relax Label</title>
<link rel="stylesheet" href="https://fonts.googleapis.com/css2?family=Barlow:wght@400;500;600;700&display=swap">
<style>
  :root {
    --page-bg: #ffffff;
    --navy: #1f2a6b;
    --navy-text: #1e2a66;
    --pink: #e89ab4;
    --pink-mid: #dc94ad;
    --lilac: #b9a3d6;
    --periwinkle: #8b97d8;
    --periwinkle-deep: #7e8bd0;
    --white: #ffffff;
    --accent-blue: #2f7fe0;
  }
  * { box-sizing: border-box; margin: 0; padding: 0; }
  html, body {
    width: 1200px; height: 750px; overflow: hidden;
    background: var(--page-bg);
    font-family: "Barlow", sans-serif;
  }
  .canvas {
    position: relative; width: 1200px; height: 750px;
    display: flex; align-items: center; justify-content: center;
  }
  .label {
    position: relative; width: 450px; height: 600px; overflow: hidden;
    background: linear-gradient(180deg,
      var(--pink) 0%, var(--pink-mid) 40%, var(--pink) 50%,
      var(--lilac) 62%, var(--periwinkle) 75%, var(--periwinkle-deep) 100%);
    text-align: center;
  }
  .callout-band {
    height: 50px; background: var(--navy);
    display: flex; align-items: center; justify-content: center;
    color: var(--white); font-size: 11px; font-weight: 600;
    letter-spacing: 0.55em;
  }
  .brand {
    margin-top: 42px; color: var(--navy-text); font-weight: 400;
    line-height: 1;
  }
  .brand-name { display: block; font-size: 70px; letter-spacing: 0.04em; }
  .brand-sub { display: block; font-size: 22px; letter-spacing: 0.22em; margin-top: 2px; }
  .function-name {
    margin-top: 62px; color: var(--white); font-weight: 700;
    font-size: 48px; letter-spacing: 0.62em; padding-left: 0.62em;
    line-height: 1; opacity: 0.92;
  }
  .function-rule { display: block; margin: 2px auto 0; }
  .product-type {
    margin-top: 2px; color: var(--navy-text); font-weight: 500; font-size: 18px;
  }
  .product-desc {
    margin-top: 6px; color: var(--white); font-weight: 500; font-size: 13.5px;
    letter-spacing: 0.06em; line-height: 1.35;
  }
  .flavour {
    margin-top: 62px; color: var(--navy-text); font-weight: 500; font-size: 22px;
    letter-spacing: 0.02em;
  }
  .volume {
    position: absolute; left: 0; right: 0; bottom: 24px;
    color: var(--white); font-weight: 700; font-size: 15px;
  }
</style>
</head>
<body>
  <main class="canvas">
    <section class="label" aria-label="Relax sparkling water front label">
      <div class="callout-band">100% NATURAL - SUGAR FREE</div>
      <h1 class="brand">
        <span class="brand-name">SOLACE</span>
        <span class="brand-sub">drinks</span>
      </h1>
      <h2 class="function-name">RELAX</h2>
      <svg class="function-rule" width="400" height="20" viewBox="0 0 400 20" aria-hidden="true">
        <path d="M4 18 Q200 -6 396 18" fill="none" stroke="var(--accent-blue)" stroke-width="2"/>
        <path d="M4 18 Q200 -4 396 18" fill="none" stroke="var(--navy)" stroke-width="1" opacity="0.6"/>
      </svg>
      <p class="product-type">Sparkling Water</p>
      <p class="product-desc">With adaptogens to help you<br>adapt to life stressors</p>
      <p class="flavour">Native Strawberry Gum</p>
      <p class="volume">330mL</p>
    </section>
  </main>
</body>
</html>
```